Nectarine Point of Sale Cards for Grocery Retail Markets

We are looking to update our Nectarine point of sale card and price card. The cards will need to be 7" x 11" with a .125 bleed - one sided. See attached for the old versions. We would like this to use photos that look like true Washington State Peaches. Here are the bullet points we would like to use: - New Crop!- Tree Ripened- Excellent FlavorNOTE: The price card just needs to have a space where a retailer can write in the sale price of the item. See attachment with the white box.

Target Market(s)

Retail market shoppers

Requirements
Must have
• Pictures of Nectarines Only

```html
<!DOCTYPE html>
<html lang="en">
<head>
<meta charset="utf-8">
<title>Washington State Nectarines – Point of Sale Card</title>
<link rel="stylesheet" href="https://fonts.googleapis.com/css2?family=Montserrat:wght@600;700;800&family=Kaushan+Script&display=swap">
<style>
  :root {
    --backdrop: #e6e6e6;
    --card-white: #f3f3f3;
    --brand-red: #c8232b;
    --ring-red: #c6212a;
    --council-green: #1d7a3c;
    --fruit-deep: #a8141c;
    --fruit-mid: #d2402a;
    --fruit-warm: #e8843e;
    --ink: #111111;
    --white: #ffffff;
  }
  * { box-sizing: border-box; margin: 0; padding: 0; }
  html, body {
    width: 1200px; height: 1000px; overflow: hidden;
    background: var(--backdrop);
  }
  .pos-card {
    position: absolute; left: 182px; top: 225px;
    width: 846px; height: 540px;
    background: var(--card-white);
  }
  .pos-card__title {
    position: absolute; left: 0; top: 0; width: 100%; height: 70px;
    display: flex; align-items: center; justify-content: center;
    font-family: "Montserrat", Arial, sans-serif;
    font-weight: 700; font-size: 41px; letter-spacing: 0.3px;
    color: var(--brand-red);
  }
  .pos-card__art { position: absolute; left: 0; top: 0; width: 846px; height: 540px; }
  .council-box {
    position: absolute; left: 50px; top: 205px; width: 238px; height: 75px;
    background: var(--white); border: 6px solid var(--brand-red);
    display: flex; align-items: center; gap: 10px; padding: 0 10px;
  }
  .council-box__dot {
    flex: none; width: 48px; height: 48px; border-radius: 50%;
    background: var(--fruit-mid);
  }
  .council-box__name {
    font-family: "Montserrat", Arial, sans-serif;
    font-weight: 700; font-size: 15px; line-height: 1.15;
    color: var(--council-green);
  }
  .price-box {
    position: absolute; left: 50px; top: 290px; width: 238px; height: 97px;
    background: var(--card-white); border: 6px solid var(--brand-red);
  }
  .tagline {
    position: absolute; left: 380px; top: 190px; width: 300px;
    text-align: center; color: var(--white);
    font-family: "Kaushan Script", cursive;
    line-height: 0.95; text-shadow: 0 2px 4px rgba(0,0,0,0.3);
  }
  .tagline__big { display: block; font-size: 64px; }
  .tagline__mid { display: block; font-size: 50px; }
  .tagline__end { display: block; font-size: 50px; }
  .benefit {
    position: absolute; width: 72px; height: 72px;
    left: 694px; display: flex; align-items: center; justify-content: center;
    text-align: center;
    font-family: "Kaushan Script", cursive;
    font-size: 14px; line-height: 1.05; color: var(--ink);
  }
  .benefit--crop { top: 147px; }
  .benefit--ripe { top: 256px; }
  .benefit--flavor { top: 363px; }
</style>
</head>
<body>
  <main class="pos-card">
    <svg class="pos-card__art" viewBox="0 0 846 540" aria-hidden="false">
      <defs>
        <radialGradient id="fruitTones" cx="50%" cy="50%" r="70%">
          <stop offset="0" stop-color="var(--fruit-mid)" stop-color-fallback="#d2402a"/>
          <stop offset="0.6" stop-color="#c0262a"/>
          <stop offset="1" stop-color="#e8843e"/>
        </radialGradient>
        <radialGradient id="fruitInner" cx="45%" cy="45%" r="60%">
          <stop offset="0" stop-color="#b81a22"/>
          <stop offset="1" stop-color="#d9603a"/>
        </radialGradient>
      </defs>
      <rect class="fruit-photo" x="0" y="70" width="846" height="448" fill="url(#fruitTones)"
            role="img" aria-label="Photo of a pile of ripe red nectarines"/>
      <circle class="ring" cx="530" cy="293" r="207" fill="#c6212a"/>
      <circle class="ring__photo" cx="530" cy="293" r="157" fill="url(#fruitInner)" stroke="#ffffff" stroke-width="4"
              role="img" aria-label="Close-up photo of nectarines"/>
      <g class="benefit-badges" fill="#ffffff" stroke="#c6212a" stroke-width="6">
        <circle cx="730" cy="183" r="36"/>
        <circle cx="730" cy="292" r="36"/>
        <circle cx="730" cy="399" r="36"/>
      </g>
    </svg>

    <h1 class="pos-card__title">WASHINGTON STATE NECTARINES</h1>

    <div class="council-box">
      <span class="council-box__dot"></span>
      <span class="council-box__name">Cascade Orchard<br>Council</span>
    </div>
    <div class="price-box" aria-label="Space for sale price"></div>

    <p class="tagline">
      <span class="tagline__big">Taste</span>
      <span class="tagline__mid">the</span>
      <span class="tagline__end">Difference</span>
    </p>

    <p class="benefit benefit--crop">New<br>Crop!</p>
    <p class="benefit benefit--ripe">Tree<br>Ripened</p>
    <p class="benefit benefit--flavor">Excellent<br>Flavor</p>
  </main>
</body>
</html>
```